New Website Design (Uncoded) Competition for Velto Trade Link

Please submit design concepts for a Joomla 3.0 Website for VELTO TRADE LINK company. Our client prefers a modem style design, responsive to all mobile devices,
The website demo content needs to be clear and detailed.

Menu sample:
Home/About Us/Service/Strength/Partner/News/Contact US/Blog

Requirements:
1. Only need to submit the PSD for the design, coding work is not included.
2. Please submit both Homepage and Inner page to demonstrate the concept.
3. The Homepage needs to include: LOGO/MENU/Banner/Language Switcher/Company Introduction/Welcome module/Advertising Module/Footer Menu/Footer/Copyright/Social Links
4. Use Asian business women for demo pictures/Could try city pictures for background.
5. Prefer SINGLE SCREEN design rather than scrollable multiple screen designs.
6. Avoid any chain symbol since the company is more about financial business.
7. Avoid any direct connotations related with money or cash.
Updates

Hi Designers, I have clearly state the requirements that avoid using neg connontation pictures like cash/ property, though still receive concepts like that. Please check the brief clearly and mark at Update with "cheers" Kip from LW

Target Market(s)

Shenzhen Dorvik Velto Trade link Company provide cross-border Supply chain Financial service by integrating Dorvik Trade Link resource.
The Company mission is become the most respectful, professional and valuable Chinese Supply Chain Financial Company, pioneer the supply chain industry.

Industry/Entity Type

Financial

Font styles to use
Sans Serif

Colors
33b7a4

Requirements
Must have
• 1. Necessary Web element, including Logo/navigation/ Banner/ Footer
2. Asia business Women pictures.
Should not have
• 6. Avoid any chain symbol since the company is more about financial business.

```html
<!DOCTYPE html>
<html lang="en">
<head>
<meta charset="utf-8">
<title>Velto Trade Link</title>
<link rel="stylesheet" href="https://fonts.googleapis.com/css2?family=Arimo:wght@400;700&family=Questrial&display=swap">
<style>
:root{
  --brand-blue:#0a4d86;
  --header-bg:#efefef;
  --nav-bg:rgba(38,135,210,.82);
  --nav-line:rgba(255,255,255,.35);
  --logo-grey:#555555;
  --phone-blue:#1a5fa8;
  --footer-bg:#0b4a82;
  --panel-bg:rgba(225,230,238,.82);
  --body-text:#444444;
  --white:#ffffff;
}
*{margin:0;padding:0;box-sizing:border-box}
html,body{width:1200px;height:946px;overflow:hidden}
body{position:relative;font-family:"Arimo",Arial,sans-serif;background:var(--white)}
.top-bar{position:absolute;left:0;top:0;width:1200px;height:5px;background:var(--brand-blue)}
.site-header{position:absolute;left:0;top:5px;width:1200px;height:126px;background:var(--header-bg);border-bottom:1px solid #d8d8d8}
.logo{position:absolute;left:143px;top:40px;display:flex;align-items:center;gap:12px}
.logo-mark{width:40px;height:40px;border-radius:50%;background:#2a8ad4}
.logo-name{font-weight:700;font-size:34px;color:var(--logo-grey);letter-spacing:1px}
.lang-switch{position:absolute;left:982px;top:8px;display:flex;align-items:center;gap:11px;font-size:14px;color:var(--phone-blue)}
.lang-flag{width:24px;height:16px;background:#1d3f7a}
.phone{position:absolute;right:133px;top:44px;font-size:17px;color:var(--phone-blue)}
.hero{position:absolute;left:0;top:131px;width:1200px;height:675px;
  background:linear-gradient(180deg,#3f7fc4 0%,#8fb8de 40%,#c9c2b0 58%,#5f7e9c 72%,#1d3a64 100%)}
.main-nav{position:absolute;left:132px;top:131px;width:234px;height:343px;background:var(--nav-bg)}
.main-nav ul{list-style:none}
.main-nav li{height:37.5px;border-bottom:1px solid var(--nav-line);display:flex;align-items:center;justify-content:center;font-size:15.5px;color:var(--white)}
.main-nav li:first-child{height:47px;padding-top:10px}
.ad-module{position:absolute;left:132px;top:474px;width:234px;height:332px;
  background:linear-gradient(180deg,#f3f0dc 0%,#ece9d2 70%,#e6f0ee 100%)}
.banner-title{position:absolute;left:392px;top:177px;width:643px;height:119px;background:rgba(70,130,160,.55);
  padding:6px 12px;font-family:"Questrial",sans-serif;color:var(--white)}
.banner-title h1{font-weight:400;font-size:36px;line-height:42px}
.banner-title p{font-size:21px;line-height:33px}
.intro-panel{position:absolute;left:379px;top:587px;width:693px;height:215px;background:var(--panel-bg);border-radius:4px;
  padding:20px 13px;font-size:11.5px;line-height:22.5px;color:var(--body-text);overflow:hidden}
.intro-panel p+p{margin-top:22.5px}
.footer-rule{position:absolute;left:0;top:806px;width:1200px;height:5px;background:var(--white)}
.site-footer{position:absolute;left:0;top:811px;width:1200px;height:135px;background:var(--footer-bg);color:var(--white)}
.footer-nav{position:absolute;left:142px;top:27px;font-size:11.5px;display:flex;gap:0}
.footer-nav span.sep{margin:0 16px}
.copyright{position:absolute;left:143px;top:75px;font-size:11.5px}
.social{position:absolute;left:916px;top:16px;display:flex;gap:16px}
.social span{width:45px;height:45px;border-radius:50%;background:#5b93c7;display:block}
.social span:nth-child(2){background:#2f87c9}
.social span:nth-child(3){background:#5682b0}
.footer-logo{position:absolute;left:918px;top:85px;display:flex;align-items:center;gap:8px;opacity:.35}
.footer-logo .logo-mark{width:26px;height:26px;background:#3d7fc1}
.footer-logo .logo-name{font-size:22px;color:#2a5f95}
</style>
</head>
<body>
<div class="top-bar"></div>
<header class="site-header">
  <div class="logo"><span class="logo-mark"></span><span class="logo-name">VELTO TRADE LINK</span></div>
  <div class="lang-switch"><span class="lang-flag" role="img" aria-label="English language flag"></span>English</div>
  <div class="phone">(555) 410-2736</div>
</header>
<section class="hero" role="img" aria-label="City skyline with harbour and sailing boats reflected in the river"></section>
<nav class="main-nav">
  <ul>
    <li>Home</li><li>About Us</li><li>Service</li><li>Strength</li><li>Partner</li><li>News</li><li>Contact US</li><li>Blog</li>
  </ul>
</nav>
<aside class="ad-module" role="img" aria-label="Advertising banner for a partner bank service"></aside>
<div class="banner-title">
  <h1>Shenzhen Dorvik Velto Trade link</h1>
  <p>Company provide cross-border Supply chain Financial service by integrating Dorvik Trade Link resource.</p>
</div>
<section class="intro-panel">
  <p>Lorem ipsum dolor sit amet, consectetur adipiscing elit. Praesent ex nunc, cursus cursus tincidunt a, pulvinar id ante. Vestibulum vitae feugiat nisl, in luctus ante. Donec sit amet suscipit felis, eget tincidunt libero. Nam sit amet fringilla mauris. Donec quis tincidunt nisi. Vivamus ultrices ligula in ex luctus bibendum. Nunc ac lacinia tortor. Sed tellus lacus, fringilla non volutpat ac, efficitur eu nulla. Nullam ornare urna vel accumsan mattis. Morbi dictum sagittis nisl, vitae scelerisque sapien luctus non. Sed vitae nisl ipsum. Integer vel elit ligula.</p>
  <p>Phasellus sem ipsum, egestas nec luctus non, ultrices nec libero. Cras hendrerit ex blandit, faucibus mauris vel, vehicula nisi. Nam sit amet mattis mi. Suspendisse a est ac sapien tincidunt blandit eu sed sem. Nullam venenatis est et venenatis semper. Morbi hendrerit</p>
</section>
<div class="footer-rule"></div>
<footer class="site-footer">
  <div class="footer-nav">
    <span>Home</span><span class="sep">/</span><span>About Us</span><span class="sep">/</span><span>Service</span><span class="sep">/</span><span>Strength</span><span class="sep">/</span><span>Partner</span><span class="sep">/</span><span>News</span><span class="sep">/</span><span>Contact US</span><span class="sep">/</span><span>Blog</span>
  </div>
  <div class="copyright">Copyright 2014 Velto Trade Link. All Rights Reserved</div>
  <div class="social">
    <span role="img" aria-label="Professional network profile"></span>
    <span role="img" aria-label="Microblog profile"></span>
    <span role="img" aria-label="Social network page"></span>
  </div>
  <div class="footer-logo"><span class="logo-mark"></span><span class="logo-name">VELTO TRADE LINK</span></div>
</footer>
</body>
</html>
```